International Flower distributer needs a landing page

We are looking to have a landing page made that will be easy to maintain and upload more content as our business grows.

We like the template designs and ease of use of Pagelofty. We'd explore other host sites.

Hello,

To start we would like something that can be managed and updated on a platform like pagelofty. We like page lofty because of the premade designs and flexibility.

Website requirements:

- About us:

- Verdant Hollow Corp - Established 1999

- Marla Pruett - Founder

- Danielle Pruett - Account Executive

- Gerald Pruett - Director of Operations

- Rosalba Penwick - (Jill's Job Description?)

- Natalia Ferreira (Make us look like a bigger company with more staff)

What we do:

- Personalized Customer service

- Exclusively Mass market experience to meet high demands

- Dedicated team assigned to your account

How we do it:

- Partnerships with farms in COlombia, ecuador and costa rica

- Farm fresh delivered directly from cargo planes to state of the art cooler facility at Delmont Airport

- Canopy trust?

Products we Sell:

- Farm made bouquets

- Consumer Bunches

- Programs Tailored to fit customer's retail program

For more Information:

- Gerald and Danielle phone and email

- Submit email inquiry

Corporate buyers that want to verify who we are and get our contact information

Floral, but not a flower shop. We import farm fresh cut flowers from south america and send them directly to supermarkets around the country.

• We are not selling anything on the website. We sell business to business.

```html
<!DOCTYPE html>
<html lang="en">
<head>
<meta charset="utf-8">
<title>Verdant Hollow – International Flower Distributor</title>
<link href="https://fonts.googleapis.com/css2?family=Montserrat:wght@400;500;600;700;800&family=Poppins:wght@400;500;600&display=swap" rel="stylesheet">
<style>
:root{
  --green:#7cc242;
  --green-dark:#5fa52c;
  --navy:#2e2f8e;
  --ink:#333;
  --muted:#666;
  --paper:#f4f4f4;
  --white:#fff;
}
*{box-sizing:border-box;margin:0;padding:0}
html,body{width:1200px;height:4032px;overflow:hidden}
body{font-family:"Poppins",sans-serif;color:var(--ink);background:var(--white);position:relative}
h1,h2,h3,.brand,.btn{font-family:"Montserrat",sans-serif}
.btn{display:inline-block;background:var(--green);color:#fff;font-size:15px;font-weight:600;padding:12px 28px;border-radius:3px}
.btn.navy{background:var(--navy)}
.section-title{text-align:center;color:var(--navy);font-size:36px;font-weight:800;letter-spacing:1px}
.divider{display:block;margin:14px auto 0}

/* header */
.site-header{position:absolute;top:0;left:0;width:1200px;height:88px;background:#fff;display:flex;align-items:center;padding:0 150px}
.brand{display:flex;align-items:center;gap:10px;color:var(--navy);font-weight:800;font-size:22px;line-height:1;text-transform:uppercase}
.brand-dot{width:44px;height:44px;border-radius:50%;background:var(--green)}
.header-right{margin-left:auto;display:flex;flex-direction:column;align-items:flex-end;gap:10px}
.top-contact{display:flex;gap:22px;font-size:12px;color:var(--muted);align-items:center}
.top-contact span{display:flex;align-items:center;gap:6px}
.nav{display:flex;gap:22px;font-size:13px;font-family:"Montserrat",sans-serif;color:var(--ink)}
.nav a{color:inherit;text-decoration:none}
.nav .active{color:var(--green);border-bottom:2px solid var(--green);padding-bottom:2px}

/* hero */
.hero{position:absolute;top:88px;left:0;width:1200px;height:632px;
  background:linear-gradient(180deg,#5a6b3e 0%,#4a5a32 40%,#7a3a2e 75%,#3a2a22 100%)}
.hero::after{content:"";position:absolute;inset:0;background:rgba(0,0,0,.35)}
.hero-text{position:absolute;z-index:1;top:340px;width:100%;text-align:center;color:#fff}
.hero-text h1{font-size:60px;font-weight:800;line-height:1.05;letter-spacing:1px}
.hero-text p{font-size:20px;margin:10px 0 22px}

/* about */
.about{position:absolute;top:720px;left:0;width:1200px;height:780px}
.about-photo{position:absolute;left:160px;top:70px;width:380px;height:380px;border-radius:50%;border:14px solid var(--navy);
  background:radial-gradient(circle at 50% 40%,#8aa06a,#5e7a40 60%,#9a4a3a)}
.since{position:absolute;left:455px;top:345px;width:100px;height:100px;border-radius:50%;background:var(--green);border:5px solid #fff;color:#fff;
  text-align:center;font-family:"Montserrat",sans-serif;font-size:13px;padding-top:22px;line-height:1.1}
.since b{display:block;font-size:26px;font-weight:800}
.about-copy{position:absolute;left:600px;top:100px;width:440px;font-size:14px;line-height:1.6;color:var(--muted)}
.about-copy .eyebrow{color:var(--green);font-weight:600;font-family:"Montserrat",sans-serif;font-size:15px}
.about-copy h2{color:var(--navy);font-size:30px;font-weight:800;margin-bottom:10px}
.about-copy .lead{color:var(--navy);font-weight:500;margin-bottom:8px}
.about-copy p+p{margin-top:8px}
.team{position:absolute;top:520px;left:90px;width:1020px;display:flex;align-items:flex-start;justify-content:space-between}
.arrow{width:36px;height:36px;border-radius:50%;border:1px solid #ccc;display:flex;align-items:center;justify-content:center;margin-top:40px}
.member{width:150px;text-align:center}
.member .avatar{width:110px;height:110px;border-radius:50%;margin:0 auto 10px;background:linear-gradient(160deg,#d9d4cc,#a9a39a)}
.member:nth-child(2) .avatar,.member:nth-child(6) .avatar{background:linear-gradient(160deg,var(--green),var(--green-dark))}
.member h3{font-size:12px;color:var(--navy);font-weight:700;text-transform:uppercase}
.member p{font-size:11px;color:var(--muted)}

/* what we do */
.what{position:absolute;top:1500px;left:0;width:1200px;height:480px;background:var(--paper);padding-top:70px}
.what-items{display:flex;justify-content:center;gap:70px;margin-top:50px}
.what-item{width:240px;text-align:center;font-size:15px;color:var(--ink);line-height:1.4}
.what-icon{width:80px;height:80px;border-radius:50%;background:var(--green);margin:0 auto 18px;display:flex;align-items:center;justify-content:center}
.what .cta{text-align:center;margin-top:34px}

/* how */
.how{position:absolute;top:1980px;left:0;width:1200px;height:600px;padding-top:80px}
.how-cards{position:relative;height:400px;margin-top:40px}
.card{position:absolute;background:#fff;box-shadow:0 4px 16px rgba(0,0,0,.12);font-size:14px;text-align:center;color:var(--ink)}
.card .pic{width:100%}
.card p{padding:14px 16px;line-height:1.4}
.card.side{width:280px;top:40px}
.card.side .pic{height:190px}
.card.center{left:460px;top:0;width:280px;height:390px;background:var(--navy);color:#fff}
.card.center .pic{height:100%;background:linear-gradient(180deg,#e8905a 0%,#c05a6a 40%,#7a3f8a 70%,#3a2a5a 100%)}
.card.center p{position:absolute;left:0;right:0;bottom:40px;text-shadow:0 1px 3px rgba(0,0,0,.6)}

/* products */
.products{position:absolute;top:2580px;left:0;width:1200px;height:760px;background:var(--paper);padding-top:90px}
.prod-grid{position:absolute;top:220px;left:160px;width:880px;display:grid;grid-template-columns:280px 280px 280px;column-gap:20px;row-gap:10px}
.prod-pic{height:220px}
.prod-text{text-align:center;padding:20px 20px 0;font-size:14px;color:var(--muted);line-height:1.5}
.prod-text h3{color:var(--navy);font-size:16px;font-weight:800;text-transform:uppercase;margin-bottom:8px}
.mini-arrow{width:30px;height:30px;border-radius:50%;border:1px solid #bbb;margin:14px auto 0;display:flex;align-items:center;justify-content:center}

/* contact */
.contact{position:absolute;top:3340px;left:0;width:1200px;height:620px;background:var(--green)}
.contact-card{position:absolute;left:280px;top:55px;width:760px;height:510px;background:#f1f6ea;padding:50px 60px;text-align:center}
.contact-card h2{color:var(--navy);font-size:32px;font-weight:800}
.contacts{display:flex;margin-top:40px;text-align:left}
.person{flex:1;padding:0 20px}
.person+.person{border-left:1px solid #cfd8c4}
.person h3{color:var(--navy);font-size:26px;font-weight:800;margin-bottom:20px}
.line{display:flex;align-items:center;gap:14px;margin-bottom:18px;font-size:13px;color:var(--ink)}
.line small{display:block;color:var(--muted);font-size:12px}
.ico{width:40px;height:40px;border-radius:50%;background:var(--navy);display:flex;align-items:center;justify-content:center;flex:none}
.contact-card .btn{margin-top:20px}

/* footer */
.site-footer{position:absolute;top:3960px;left:0;width:1200px;height:72px;background:#fff;text-align:center;font-size:12px;color:var(--muted);padding-top:12px}
.social{display:flex;justify-content:center;gap:10px;margin-top:8px}
.social span{width:24px;height:24px;border-radius:50%;background:var(--green)}
</style>
</head>
<body>

<header class="site-header">
  <div class="brand"><span class="brand-dot"></span><span>Verdant<br>Hollow</span></div>
  <div class="header-right">
    <div class="top-contact">
      <span><svg width="12" height="12" viewBox="0 0 24 24"><path fill="#7cc242" d="M6.6 10.8a15 15 0 006.6 6.6l2.2-2.2c.3-.3.7-.4 1-.2 1.1.4 2.3.6 3.6.6.6 0 1 .4 1 1V20c0 .6-.4 1-1 1A17 17 0 013 4c0-.6.4-1 1-1h3.5c.6 0 1 .4 1 1 0 1.3.2 2.5.6 3.6.1.3 0 .7-.2 1z"/></svg>786-555-0142</span>
      <span><svg width="12" height="12" viewBox="0 0 24 24"><path fill="#7cc242" d="M12 2a7 7 0 00-7 7c0 5 7 13 7 13s7-8 7-13a7 7 0 00-7-7zm0 9.5A2.5 2.5 0 1112 6a2.5 2.5 0 010 5.5z"/></svg>4120 Harbor Lane, Delmont FL 33000</span>
    </div>
    <nav class="nav">
      <a class="active">Home</a><a>About</a><a>What We Do</a><a>How We Do It</a><a>Products We Sell</a><a>Contact</a>
    </nav>
  </div>
</header>

<section class="hero" role="img" aria-label="Farm workers harvesting fresh flowers in a field">
  <div class="hero-text">
    <h1>INTERNATIONAL<br>FLOWER DISTRIBUTOR</h1>
    <p>We Import Farm Fresh Cut Flowers And Send Directly To Supermarkets</p>
    <span class="btn">Contact Us Today ›</span>
  </div>
</section>

<section class="about">
  <div class="about-photo" role="img" aria-label="Grower holding a crate of freshly cut flowers"></div>
  <div class="since">Since<b>1999</b></div>
  <div class="about-copy">
    <div class="eyebrow">ABOUT</div>
    <h2>VERDANT HOLLOW</h2>
    <p class="lead">Growing trusted partnerships with supermarkets since 1999.</p>
    <p>Verdant Hollow Corp imports farm fresh cut flowers from South America and ships them directly to supermarkets across the country. Our team handles every step from farm to store so buyers receive consistent quality and reliable volume.</p>
    <p>We work only business to business, pairing each retail partner with a dedicated account team that knows their program, their season and their customers, and keeps every order fresh and on time.</p>
  </div>
  <div class="team">
    <span class="arrow"><svg width="12" height="12" viewBox="0 0 12 12"><path d="M8 1L3 6l5 5" stroke="#666" fill="none" stroke-width="1.5"/></svg></span>
    <div class="member"><div class="avatar" role="img" aria-label="Portrait of Marla Pruett"></div><h3>Marla Pruett</h3><p>Founder</p></div>
    <div class="member"><div class="avatar" role="img" aria-label="Portrait of Rosalba Penwick"></div><h3>Rosalba Penwick</h3><p>Jill's Job Description</p></div>
    <div class="member"><div class="avatar" role="img" aria-label="Portrait of Gerald Pruett"></div><h3>Gerald Pruett</h3><p>Director of Operations</p></div>
    <div class="member"><div class="avatar" role="img" aria-label="Portrait of Danielle Pruett"></div><h3>Danielle Pruett</h3><p>Account Executive</p></div>
    <div class="member"><div class="avatar" role="img" aria-label="Portrait of Natalia Ferreira"></div><h3>Natalia Ferreira</h3><p>Team Member</p></div>
    <span class="arrow"><svg width="12" height="12" viewBox="0 0 12 12"><path d="M4 1l5 5-5 5" stroke="#666" fill="none" stroke-width="1.5"/></svg></span>
  </div>
</section>

<section class="what">
  <h2 class="section-title">WHAT WE DO</h2>
  <svg class="divider" width="24" height="24" viewBox="0 0 24 24"><rect x="5" y="5" width="14" height="14" transform="rotate(45 12 12)" fill="none" stroke="#7cc242" stroke-width="2"/></svg>
  <div class="what-items">
    <div class="what-item"><div class="what-icon"><svg width="36" height="36" viewBox="0 0 24 24"><circle cx="12" cy="8" r="4" fill="#fff"/><path d="M4 21c0-4 4-7 8-7s8 3 8 7z" fill="#fff"/></svg></div>Personalized<br>Customer Service</div>
    <div class="what-item"><div class="what-icon"><svg width="36" height="36" viewBox="0 0 24 24"><path d="M4 20V10h4v10zm6 0V4h4v16zm6 0v-7h4v7z" fill="#fff"/></svg></div>Exclusively Mass market<br>experience to meet high demands</div>
    <div class="what-item"><div class="what-icon"><svg width="36" height="36" viewBox="0 0 24 24"><circle cx="7" cy="9" r="3" fill="#fff"/><circle cx="17" cy="9" r="3" fill="#fff"/><path d="M1 20c0-3 3-5 6-5s6 2 6 5zm10 0c0-3 3-5 6-5s6 2 6 5z" fill="#fff"/></svg></div>Dedicated Team Assigned<br>To Your Account</div>
  </div>
  <div class="cta"><span class="btn navy">Contact Us Today ›</span></div>
</section>

<section class="how">
  <h2 class="section-title">HOW WE DO IT</h2>
  <svg class="divider" width="24" height="24" viewBox="0 0 24 24"><rect x="5" y="5" width="14" height="14" transform="rotate(45 12 12)" fill="none" stroke="#7cc242" stroke-width="2"/></svg>
  <div class="how-cards">
    <div class="card side" style="left:160px"><div class="pic" role="img" aria-label="Partner growers at a flower farm" style="background:linear-gradient(160deg,#8cb36a,#c8a070)"></div><p>Partnerships With Farms in Colombia, Ecuador &amp; Costa Rica</p></div>
    <div class="card center"><div class="pic" role="img" aria-label="Cargo plane flying over a flower field at sunset"></div><p>Farm fresh delivered directly from cargo planes to state of the art cooler facility at Delmont Airport</p></div>
    <div class="card side" style="left:760px"><div class="pic" role="img" aria-label="Worker tending roses in a greenhouse" style="background:linear-gradient(160deg,#4f7a3a,#b8454a)"></div><p>Canopy Trust</p></div>
  </div>
</section>

<section class="products">
  <h2 class="section-title">PRODUCTS WE SELL</h2>
  <svg class="divider" width="24" height="24" viewBox="0 0 24 24"><rect x="5" y="5" width="14" height="14" transform="rotate(45 12 12)" fill="none" stroke="#7cc242" stroke-width="2"/></svg>
  <div class="prod-grid">
    <div class="prod-pic" role="img" aria-label="Rows of yellow chrysanthemums on a farm" style="background:linear-gradient(160deg,#c9c25a,#6d8a3a)"></div>
    <div class="prod-text"><h3>Consumer<br>Bunches</h3>Ready to sell bunches packed for supermarket shelves and checkout displays.<div class="mini-arrow"><svg width="10" height="10" viewBox="0 0 12 12"><path d="M4 1l5 5-5 5" stroke="#666" fill="none" stroke-width="1.5"/></svg></div></div>
    <div class="prod-pic" role="img" aria-label="Account team meeting with a retail buyer" style="background:linear-gradient(160deg,#d8d2c8,#8f8a82)"></div>
    <div class="prod-text"><h3>Farm Made<br>Bouquets</h3>Bouquets designed and assembled at the farm, shipped fresh to your stores.<div class="mini-arrow"><svg width="10" height="10" viewBox="0 0 12 12"><path d="M4 1l5 5-5 5" stroke="#666" fill="none" stroke-width="1.5"/></svg></div></div>
    <div class="prod-pic" role="img" aria-label="Mixed bouquet of purple and white flowers" style="background:linear-gradient(160deg,#8a74b8,#3a3550)"></div>
    <div class="prod-text"><h3>Programs Tailored<br>To Fit Customer's<br>Retail Program</h3>Flexible programs built around your volume, season and price points.<div class="mini-arrow"><svg width="10" height="10" viewBox="0 0 12 12"><path d="M4 1l5 5-5 5" stroke="#666" fill="none" stroke-width="1.5"/></svg></div></div>
  </div>
</section>

<section class="contact">
  <div class="contact-card">
    <h2>FOR MORE INFORMATION</h2>
    <div class="contacts">
      <div class="person">
        <h3>GERALD PRUETT</h3>
        <div class="line"><span class="ico"><svg width="18" height="18" viewBox="0 0 24 24"><path fill="#fff" d="M6.6 10.8a15 15 0 006.6 6.6l2.2-2.2c.3-.3.7-.4 1-.2 1.1.4 2.3.6 3.6.6.6 0 1 .4 1 1V20c0 .6-.4 1-1 1A17 17 0 013 4c0-.6.4-1 1-1h3.5c.6 0 1 .4 1 1 0 1.3.2 2.5.6 3.6.1.3 0 .7-.2 1z"/></svg></span><div><small>Phone</small>786-555-0188</div></div>
        <div class="line"><span class="ico"><svg width="18" height="18" viewBox="0 0 24 24"><path fill="#fff" d="M3 5h18v14H3zm2 2v.5l7 4.5 7-4.5V7z"/></svg></span><div><small>Email</small>gerald@verdanthollowcorp.com</div></div>
      </div>
      <div class="person">
        <h3>DANIELLE PRUETT</h3>
        <div class="line"><span class="ico"><svg width="18" height="18" viewBox="0 0 24 24"><path fill="#fff" d="M6.6 10.8a15 15 0 006.6 6.6l2.2-2.2c.3-.3.7-.4 1-.2 1.1.4 2.3.6 3.6.6.6 0 1 .4 1 1V20c0 .6-.4 1-1 1A17 17 0 013 4c0-.6.4-1 1-1h3.5c.6 0 1 .4 1 1 0 1.3.2 2.5.6 3.6.1.3 0 .7-.2 1z"/></svg></span><div><small>Phone</small>305-555-0167</div></div>
        <div class="line"><span class="ico"><svg width="18" height="18" viewBox="0 0 24 24"><path fill="#fff" d="M3 5h18v14H3zm2 2v.5l7 4.5 7-4.5V7z"/></svg></span><div><small>Email</small>danielle@verdanthollowcorp.com</div></div>
      </div>
    </div>
    <span class="btn navy">Send Email Inquiry ›</span>
  </div>
</section>

<footer class="site-footer">
  <p>Copyright © 2022 Verdant Hollow. All Rights Reserved.</p>
  <div class="social"><span></span><span></span><span></span><span></span></div>
</footer>

</body>
</html>
```